Business Card Design - Cryotherapy

We need a custom created business card for our company FrostLeaf Spa. We provide whole body cryotherapy and localized cryotherapy to our clients. Please be creative.
Please see our website for idea's on design.
www.frostleafspa-example.com
Industry/Entity Type
Business
Contact Information for Business Card
Name, Position, Phone Number, Address, Website, Email
Look and feel
Each slider illustrates characteristics of the customer's brand and the style your logo design should communicate.

```html
<!DOCTYPE html>
<html lang="en">
<head>
<meta charset="utf-8">
<title>FrostLeaf Spa – Business Card</title>
<link href="https://fonts.googleapis.com/css2?family=Open+Sans:wght@400;600;700&display=swap" rel="stylesheet">
<style>
  :root {
    --backdrop: #9a9a9a;
    --card-white: #ffffff;
    --teal: #4ab6b8;
    --teal-deep: #1e9fa6;
    --art-light: #6ccfc8;
    --art-mid: #37b3ad;
    --art-dark: #1f9a7c;
    --brand-green: #1c8a62;
    --text-light: #ffffff;
  }
  * { box-sizing: border-box; margin: 0; padding: 0; }
  html, body { width: 1200px; height: 900px; overflow: hidden; }
  body {
    background: var(--backdrop);
    font-family: "Open Sans", Arial, sans-serif;
    display: flex;
    flex-direction: column;
    align-items: center;
    justify-content: center;
    gap: 22px;
  }
  .card {
    position: relative;
    width: 740px;
    height: 423px;
    overflow: hidden;
    background: var(--card-white);
    box-shadow: 0 4px 14px rgba(0,0,0,0.25);
  }
  /* Front: brand card */
  .brand-card {
    display: flex;
    align-items: center;
    justify-content: center;
    gap: 18px;
  }
  .brand-dot {
    width: 46px;
    height: 46px;
    border-radius: 50%;
    background: var(--art-mid);
  }
  .brand-name {
    font-weight: 600;
    font-size: 58px;
    letter-spacing: 1px;
    color: var(--brand-green);
  }
  /* Back: contact card */
  .contact-art {
    position: absolute;
    inset: 0;
    width: 100%;
    height: 100%;
  }
  .contact-details {
    position: absolute;
    right: 40px;
    top: 110px;
    text-align: right;
    color: var(--text-light);
    font-size: 17px;
    line-height: 1.4;
  }
  .person-name {
    font-weight: 700;
    font-size: 22px;
    line-height: 1.25;
  }
  .person-role { margin-bottom: 6px; }
  .address { margin-bottom: 16px; }
  .contact-line {
    display: flex;
    justify-content: flex-end;
    align-items: center;
    gap: 12px;
  }
  .contact-icon { width: 15px; height: 15px; flex: none; }
</style>
</head>
<body>

  <section class="card brand-card">
    <span class="brand-dot"></span>
    <span class="brand-name">FrostLeaf Spa</span>
  </section>

  <section class="card contact-card">
    <svg class="contact-art" viewBox="0 0 740 423">
      <defs>
        <linearGradient id="art-fill" x1="0" y1="0" x2="1" y2="1">
          <stop offset="0" stop-color="#6ccfc8"/>
          <stop offset="0.55" stop-color="#37b3ad"/>
          <stop offset="1" stop-color="#1f9a7c"/>
        </linearGradient>
      </defs>
      <rect class="teal-panel" width="740" height="423" fill="var(--teal)"/>
      <ellipse class="swoosh-thin" cx="60" cy="170" rx="314" ry="352" fill="none" stroke="var(--teal-deep)" stroke-width="2"/>
      <ellipse class="swoosh" cx="60" cy="170" rx="300" ry="340" fill="none" stroke="var(--teal-deep)" stroke-width="6"/>
      <ellipse class="white-field" cx="60" cy="170" rx="290" ry="330" fill="var(--card-white)"/>
      <g role="img" aria-label="Illustration of a woman's profile with faceted teal hair">
        <ellipse cx="40" cy="160" rx="250" ry="260" fill="url(#art-fill)"/>
      </g>
    </svg>

    <div class="contact-details">
      <p class="person-name">Daniel Whitmore</p>
      <p class="person-role">Managing Director</p>
      <p class="address">12345, Address Goes Here<br>Country Name, 123456.</p>
      <p class="contact-line">0170 482 315
        <svg class="contact-icon" viewBox="0 0 16 16"><rect x="4" y="1" width="8" height="14" rx="1.5" fill="none" stroke="#fff" stroke-width="1.5"/><circle cx="8" cy="12.5" r="0.9" fill="#fff"/></svg>
      </p>
      <p class="contact-line">044-270 918 644
        <svg class="contact-icon" viewBox="0 0 16 16"><path d="M3 2 L6 2 L7 5.5 L5.3 6.8 A8 8 0 0 0 9.2 10.7 L10.5 9 L14 10 L14 13 A1.5 1.5 0 0 1 12.5 14.5 A11 11 0 0 1 1.5 3.5 A1.5 1.5 0 0 1 3 2 Z" fill="#fff"/></svg>
      </p>
      <p class="contact-line">info@frostleafspa-example.com
        <svg class="contact-icon" viewBox="0 0 16 16"><rect x="1.5" y="3.5" width="13" height="9" fill="none" stroke="#fff" stroke-width="1.4"/><path d="M1.5 3.5 L8 9 L14.5 3.5" fill="none" stroke="#fff" stroke-width="1.4"/></svg>
      </p>
      <p class="contact-line">www.frostleafspa-example.com
        <svg class="contact-icon" viewBox="0 0 16 16"><circle cx="8" cy="8" r="6.5" fill="none" stroke="#fff" stroke-width="1.3"/><ellipse cx="8" cy="8" rx="2.8" ry="6.5" fill="none" stroke="#fff" stroke-width="1.1"/><path d="M1.5 8 H14.5" stroke="#fff" stroke-width="1.1"/></svg>
      </p>
    </div>
  </section>

</body>
</html>
```